Business card design/logo/website name

I am a business coach. My business name is PHA (Pardee Hollis & Associates, Inc.) I want to use this card just for coaching. I do two kinds: Personal Image coach and Executive business coach
1. I work with people to become a polished global professional.
"Become a confident, savvy professional building relationships tactfully and appropriately while clearly representing your own company’s message and image.
Learn the nuances… Master the skills… Use the business etiquette techniques and protocols that allow you to seamlessly and confidently conduct business in a global business environment.
Have the comfort of knowing what to expect, what to do and how to easily build long and short-term relationships that give you the winning edge and increased company profits."
2. Leadership Coaching
For increasing the team’s productivity by building stronger relationships. Build strong compelling vision and write and share their Personal Leadership Philosophy, a roadmap that is concise and commanding and gives the team a clear vision of the leader's expectations.

PHA should be the logo. (Downplay the Pardee Hollis and Associates, Inc.)

Want:
Executive Coach
Consultant

Reason: I am traveling and connections are often broken.

Target Market(s)

Executives, business people

Industry/Entity Type

Building

Font styles to use
Sans Serif
Script

Colors
0255a3
3176b5
85acd3
ec2027

Requirements
Must have
• PHA as the logo,(no preference on how you treat PHA) with Pardee Hollis & Associates. Inc. downplayed.
On the card:
Georgette Hollis CEO
Executive Coach
Consultant
KMV 4(c)
Coaching - Training - Strategic Planning

```html
<!DOCTYPE html>
<html lang="en">
<head>
<meta charset="utf-8">
<title>PHA Business Card — Front and Back</title>
<link rel="stylesheet" href="https://fonts.googleapis.com/css2?family=Arimo:wght@400;700&display=swap">
<style>
  :root {
    --brand-blue: #0255a3;
    --mid-blue: #3176b5;
    --light-blue: #85acd3;
    --sky-blue: #5a9ad6;
    --navy: #143d6b;
    --ink: #1a3f8f;
    --stage-top: #f6f6f6;
    --stage-bottom: #d4d4d4;
  }
  * { box-sizing: border-box; margin: 0; padding: 0; }
  html, body { width: 1200px; height: 1000px; overflow: hidden; }
  body {
    background: linear-gradient(180deg, var(--stage-top), var(--stage-bottom));
    font-family: "Arimo", Arial, sans-serif;
    position: relative;
  }
  .card {
    position: absolute;
    width: 600px;
    height: 343px;
    overflow: hidden;
    box-shadow: 0 8px 22px rgba(0, 0, 0, 0.25);
  }
  .card--front {
    left: 60px;
    top: 120px;
    background: linear-gradient(160deg, #2e6fb0 0%, var(--sky-blue) 55%, #5b9bd7 100%);
  }
  .card--back {
    left: 540px;
    top: 537px;
    background: linear-gradient(180deg, var(--sky-blue) 0%, #3a78b4 38%, var(--navy) 72%, var(--navy) 100%);
  }
  .card__curves { position: absolute; inset: 0; width: 100%; height: 100%; }
  .card__rosette {
    position: absolute;
    border-radius: 50%;
    background: radial-gradient(circle, rgba(133, 172, 211, 0.45) 0%, rgba(133, 172, 211, 0.2) 55%, rgba(133, 172, 211, 0) 72%);
  }
  .card--front .card__rosette { left: 170px; top: 40px; width: 260px; height: 260px; }
  .card--back .card__rosette { left: 170px; top: 42px; width: 260px; height: 260px; }

  .brand { position: absolute; display: flex; flex-direction: column; color: var(--brand-blue); }
  .brand__mark { font-weight: 700; font-size: 64px; line-height: 1; letter-spacing: 2px; }
  .brand__name { font-weight: 400; font-size: 9px; letter-spacing: 0.5px; text-transform: uppercase; margin-top: 3px; }
  .card--front .brand { left: 38px; top: 118px; }
  .card--back .brand { left: 50%; top: 50%; transform: translate(-50%, -60%); align-items: center; }
  .card--back .brand__mark { font-size: 80px; }

  .contact { position: absolute; left: 150px; top: 210px; color: var(--ink); }
  .contact__name { font-weight: 700; font-size: 22px; margin-bottom: 10px; }
  .contact__line { font-size: 14px; line-height: 1.45; }
  .contact__services { font-size: 14px; margin-top: 2px; }
</style>
</head>
<body>
  <section class="card card--front" aria-label="Business card front">
    <svg class="card__curves" viewBox="0 0 600 343" aria-hidden="true">
      <path d="M250 0 H600 V300 C520 240 470 120 420 40 C380 60 320 70 250 0 Z" fill="#3176b5"/>
      <path d="M360 0 H600 V330 C520 230 460 110 420 40 C410 20 390 8 360 0 Z" fill="#0255a3"/>
      <path d="M250 0 C320 70 380 60 420 40 L440 0 Z" fill="#0d4f95" opacity="0.55"/>
    </svg>
    <div class="card__rosette" role="img" aria-label="Faint decorative rosette pattern"></div>
    <div class="brand">
      <span class="brand__mark">PHA</span>
      <span class="brand__name">Pardee Hollis &amp; Associates, Inc.</span>
    </div>
    <div class="contact">
      <p class="contact__name">Georgette Hollis | CEO</p>
      <p class="contact__line">Executive Coach</p>
      <p class="contact__line">Consultant</p>
      <p class="contact__line">KMV 4(c)</p>
      <p class="contact__services">Coaching - Training - Strategic Planning</p>
    </div>
  </section>

  <section class="card card--back" aria-label="Business card back">
    <div class="card__rosette" role="img" aria-label="Faint decorative rosette pattern"></div>
    <div class="brand">
      <span class="brand__mark">PHA</span>
      <span class="brand__name">Pardee Hollis &amp; Associates, Inc.</span>
    </div>
  </section>
</body>
</html>
```